Soft furnishing company selling fabrics, curtains, bedlinen craft & haberdashery

We need 4 x home page banners for our website as follows:
Image 1 - to lead customers to our "New season Fabrics" page,
Image 2 - to lead customers to our Ready Made curtains,
Image 3 - to lead customers to our "Polar Bear Bed linen" page
Image 4 - to lead customers to our "Christmas raft Tutorial" page

Banner needs to be 960px wide x 380px 72dpi and optimised for web. should have a little descriptive text for example "Fabulous Fabric. Prints, plains & weaves, view our range of new season furnishing fabrics to buy by the metre" "Instantly update your home with our range of ready made curtains. Available . "Cosy Night In. Snuggle with this Polar Bear Duvet Set. From €20" "" "Let's Get Crafting for Christmas. Download our free Project and tutoirals here. First 3 images need a "shop now" button

website url www.lintelway.ie

Target Market(s)

Female 25 -45

Industry/Entity Type

It Company

Font styles to use
Serif
Sans Serif

Requirements
Must have
• shop now button on image 1, 2, 3
Should not have
• too much text or clutter

```html
<!DOCTYPE html>
<html lang="en">
<head>
<meta charset="utf-8">
<title>Cosy Night In – Polar Bear Duvet Set</title>
<link rel="stylesheet" href="https://fonts.googleapis.com/css2?family=Arimo:wght@400&family=PT+Serif:wght@700&display=swap">
<style>
  :root {
    --satin-dark: #2e2e30;
    --satin-mid: #444446;
    --satin-light: #5a5a5c;
    --photo-light: #e6e2df;
    --photo-mid: #b9b1aa;
    --photo-dark: #8a7f76;
    --white: #ffffff;
    --ink: #111111;
    --price-red: #e0222c;
    --cta-orange: #f28321;
  }
  * { margin: 0; padding: 0; box-sizing: border-box; }
  html, body {
    width: 1200px;
    height: 475px;
    overflow: hidden;
    background: var(--white);
  }
  .banner {
    position: relative;
    width: 1200px;
    height: 475px;
    overflow: hidden;
    background:
      radial-gradient(ellipse 420px 260px at 78% 25%, var(--satin-light), transparent 70%),
      radial-gradient(ellipse 380px 220px at 95% 85%, var(--satin-mid), transparent 70%),
      linear-gradient(135deg, var(--satin-mid) 0%, var(--satin-dark) 45%, var(--satin-mid) 75%, var(--satin-dark) 100%);
    font-family: "Arimo", Arial, sans-serif;
  }
  .banner__art {
    position: absolute;
    inset: 0;
  }
  .headline {
    position: absolute;
    left: 581px;
    top: 56px;
    width: 580px;
    text-align: center;
    color: var(--white);
    font-size: 32px;
    font-weight: 400;
    line-height: 46px;
  }
  .headline__line {
    display: block;
    white-space: nowrap;
  }
  .price-badge {
    position: absolute;
    left: 813px;
    top: 208px;
    width: 130px;
    height: 130px;
  }
  .price-badge__label {
    font-family: "PT Serif", Georgia, serif;
    font-weight: 700;
    font-size: 14px;
    fill: var(--ink);
  }
  .price-badge__amount {
    font-family: "PT Serif", Georgia, serif;
    font-weight: 700;
    font-size: 44px;
    fill: var(--price-red);
  }
  .shop-button {
    position: absolute;
    left: 745px;
    top: 380px;
    width: 265px;
    height: 73px;
    border-radius: 8px;
    background: var(--cta-orange);
    color: var(--white);
    font-size: 32px;
    line-height: 73px;
    text-align: center;
    text-decoration: none;
  }
</style>
</head>
<body>
  <main class="banner">
    <svg class="banner__art" width="1200" height="475" viewBox="0 0 1200 475">
      <defs>
        <linearGradient id="bedroom-tones" x1="0" y1="0" x2="1" y2="1">
          <stop offset="0" stop-color="var(--photo-mid)"/>
          <stop offset="0.45" stop-color="var(--photo-light)"/>
          <stop offset="1" stop-color="var(--photo-dark)"/>
        </linearGradient>
        <clipPath id="photo-shape">
          <circle cx="249" cy="237.5" r="307"/>
        </clipPath>
      </defs>
      <circle class="photo-frame" cx="249" cy="237.5" r="313" fill="var(--white)"/>
      <rect class="product-photo" x="0" y="0" width="560" height="475"
            fill="url(#bedroom-tones)" clip-path="url(#photo-shape)"
            role="img" aria-label="Bedroom with a polar bear print duvet set, matching pillows, a grey armchair and a shaggy rug"/>
      <polygon class="photo-pointer" points="558,222 574,237.5 558,253" fill="var(--white)"/>
    </svg>

    <h1 class="headline">
      <span class="headline__line">Cosy Night In,</span>
      <span class="headline__line">Snuggle with this Polar Bear</span>
      <span class="headline__line">Duvet Set</span>
    </h1>

    <svg class="price-badge" viewBox="-64 -64 128 128" aria-label="From only €20">
      <polygon fill="var(--white)" points="62,0 51,10.1 57.3,23.7 43.2,28.9 43.8,43.8 28.9,43.2 23.7,57.3 10.1,51 0,62 -10.1,51 -23.7,57.3 -28.9,43.2 -43.8,43.8 -43.2,28.9 -57.3,23.7 -51,10.1 -62,0 -51,-10.1 -57.3,-23.7 -43.2,-28.9 -43.8,-43.8 -28.9,-43.2 -23.7,-57.3 -10.1,-51 0,-62 10.1,-51 23.7,-57.3 28.9,-43.2 43.8,-43.8 43.2,-28.9 57.3,-23.7 51,-10.1"/>
      <text class="price-badge__label" x="0" y="-25" text-anchor="middle">From</text>
      <text class="price-badge__label" x="0" y="-7" text-anchor="middle">Only</text>
      <text class="price-badge__amount" x="0" y="32" text-anchor="middle">€20</text>
    </svg>

    <a class="shop-button" href="#">Shop Now</a>
  </main>
</body>
</html>
```